Business Card Design

I need a business card for my tutoring service. Key elements on front are its contact details and visual appeal with these three points: All aspects of literacy and numeracy, 'Bright Pathways Support' provider and Prep-readiness sessions
Updates

contact me by email on korawen7@mailtrove.net as I'm having issues with other address at times. Thanks

:) 

Target Market(s)

People with children

Industry/Entity Type

Tutoring

Contact Information for Business Card

Tessa Brindle Educational Consultant
17 Quillon Grove
Tarrowin 4821
0487 316 912

Requirements
Nice to have
• Something related to education. On the back of the card, my business name and phone number again, along with: spelling, reading, writing, comprehension, oral language, listening skills

```html
<!DOCTYPE html>
<html lang="en">
<head>
<meta charset="utf-8">
<title>Tessa Brindle – Business Card</title>
<link href="https://fonts.googleapis.com/css2?family=Open+Sans:ital,wght@0,400;0,600;0,700;1,400&display=swap" rel="stylesheet">
<style>
  :root{
    --bg:#e6e6e6;
    --red:#d21f35;
    --red-deep:#b8182c;
    --red-band:#c91c31;
    --yellow:#ffe600;
    --white:#ffffff;
    --photo-a:#f2f2f2;
    --photo-b:#e8a13a;
    --photo-c:#3f7fd0;
  }
  *{box-sizing:border-box;margin:0;padding:0}
  html,body{width:1200px;height:1200px;overflow:hidden;background:var(--bg);font-family:"Open Sans",Arial,sans-serif}
  .card{position:absolute;left:110px;width:980px;height:540px;background:var(--red);overflow:hidden;box-shadow:0 6px 18px rgba(0,0,0,.18)}
  .card--details{top:40px}
  .card--services{top:620px}

  /* details card */
  .identity{position:absolute;left:470px;top:62px;color:var(--yellow)}
  .identity__name{font-size:40px;font-weight:700;line-height:1.1}
  .identity__role{font-size:27px;font-style:italic;color:var(--white);margin-top:2px}
  .contact{position:absolute;left:470px;top:170px;color:var(--white);font-size:29px;line-height:1.35}
  .contact__row{display:flex;align-items:flex-start;gap:10px}
  .contact__row svg{flex:none;margin-top:8px}
  .contact__indent{padding-left:32px}
  .divider{position:absolute;left:0;right:0;top:330px;height:5px;background:var(--red-deep)}
  .skills-band{position:absolute;left:0;right:0;top:335px;bottom:0;background:var(--red-band)}
  .skills{position:absolute;top:385px;display:flex;flex-direction:column;gap:4px;list-style:none}
  .skills--left{left:25px}
  .skills--right{left:245px}
  .skills li{display:flex;align-items:center;gap:14px;color:var(--yellow);font-size:27px;font-weight:600;letter-spacing:.5px}

  /* services card */
  .photo{position:absolute;left:0;top:0;width:980px;height:210px;background:linear-gradient(100deg,var(--photo-b) 0%,var(--photo-c) 45%,var(--red) 70%,var(--photo-a) 100%)}
  .services{position:absolute;left:0;right:0;top:210px;bottom:0;background:var(--red)}
  .services__title{position:absolute;left:40px;top:30px;color:var(--yellow);font-size:34px;font-weight:700;letter-spacing:2px}
  .services__list{position:absolute;left:40px;top:100px;list-style:none}
  .services__list li{display:flex;align-items:center;gap:16px;color:var(--white);font-size:38px;line-height:1.4}
</style>
</head>
<body>

<section class="card card--details">
  <div class="divider"></div>
  <div class="skills-band"></div>

  <div class="identity">
    <h1 class="identity__name">Tessa Brindle</h1>
    <p class="identity__role">Educational Consultant</p>
  </div>

  <div class="contact">
    <p class="contact__row">
      <svg width="20" height="24" viewBox="0 0 20 24" aria-hidden="true"><path d="M10 0a8 8 0 0 0-8 8c0 6 8 16 8 16s8-10 8-16a8 8 0 0 0-8-8zm0 11a3 3 0 1 1 0-6 3 3 0 0 1 0 6z" fill="var(--yellow)"/></svg>
      <span>17 Quillon Grove</span>
    </p>
    <p class="contact__indent">Tarrowin 4821</p>
    <p class="contact__row">
      <svg width="22" height="22" viewBox="0 0 24 24" aria-hidden="true"><path d="M6.6 10.8a15.1 15.1 0 0 0 6.6 6.6l2.2-2.2a1 1 0 0 1 1-.25 11.4 11.4 0 0 0 3.6.57 1 1 0 0 1 1 1V20a1 1 0 0 1-1 1A17 17 0 0 1 3 4a1 1 0 0 1 1-1h3.5a1 1 0 0 1 1 1c0 1.25.2 2.45.57 3.57a1 1 0 0 1-.25 1z" fill="var(--yellow)"/></svg>
      <span>0487.316.912</span>
    </p>
  </div>

  <ul class="skills skills--left">
    <li><svg width="24" height="24" viewBox="0 0 24 24" aria-hidden="true"><path d="M12 1l3.2 7 7.6.8-5.7 5.1 1.6 7.6L12 17.6l-6.7 3.9 1.6-7.6L1.2 8.8 8.8 8z" fill="var(--white)"/></svg>Spelling</li>
    <li><svg width="24" height="24" viewBox="0 0 24 24" aria-hidden="true"><path d="M12 1l3.2 7 7.6.8-5.7 5.1 1.6 7.6L12 17.6l-6.7 3.9 1.6-7.6L1.2 8.8 8.8 8z" fill="var(--white)"/></svg>Reading</li>
    <li><svg width="24" height="24" viewBox="0 0 24 24" aria-hidden="true"><path d="M12 1l3.2 7 7.6.8-5.7 5.1 1.6 7.6L12 17.6l-6.7 3.9 1.6-7.6L1.2 8.8 8.8 8z" fill="var(--white)"/></svg>Writing</li>
  </ul>
  <ul class="skills skills--right">
    <li><svg width="24" height="24" viewBox="0 0 24 24" aria-hidden="true"><path d="M12 1l3.2 7 7.6.8-5.7 5.1 1.6 7.6L12 17.6l-6.7 3.9 1.6-7.6L1.2 8.8 8.8 8z" fill="var(--white)"/></svg>Comprehension</li>
    <li><svg width="24" height="24" viewBox="0 0 24 24" aria-hidden="true"><path d="M12 1l3.2 7 7.6.8-5.7 5.1 1.6 7.6L12 17.6l-6.7 3.9 1.6-7.6L1.2 8.8 8.8 8z" fill="var(--white)"/></svg>Oral Language</li>
    <li><svg width="24" height="24" viewBox="0 0 24 24" aria-hidden="true"><path d="M12 1l3.2 7 7.6.8-5.7 5.1 1.6 7.6L12 17.6l-6.7 3.9 1.6-7.6L1.2 8.8 8.8 8z" fill="var(--white)"/></svg>Listening Skills</li>
  </ul>
</section>

<section class="card card--services">
  <div class="photo" role="img" aria-label="Photo of colourful wooden alphabet and number blocks stacked together"></div>
  <div class="services">
    <h2 class="services__title">TESSA BRINDLE EDUCATIONAL CONSULTANT</h2>
    <ul class="services__list">
      <li><svg width="30" height="30" viewBox="0 0 30 30" aria-hidden="true"><path d="M2 2l26 13L2 28z" fill="var(--yellow)"/></svg>All Aspect of Literacy And Numeracy</li>
      <li><svg width="30" height="30" viewBox="0 0 30 30" aria-hidden="true"><path d="M2 2l26 13L2 28z" fill="var(--yellow)"/></svg>Bright Pathways Support</li>
      <li><svg width="30" height="30" viewBox="0 0 30 30" aria-hidden="true"><path d="M2 2l26 13L2 28z" fill="var(--yellow)"/></svg>Provider And prep-Readiness Sessions</li>
    </ul>
  </div>
</section>

</body>
</html>
```